Need new website for my business

I want to design a new Irrigation website for our business. What we are looking for is to have a residential section that describes providing for irrigation service for residential customers in homeowners Association. From startups to service to winterization in full residential installs.
A commercial section on our webpage describing. installation of commercial Irrigation systems. Service start-up of systems. To winterizations. Offering contract service plans for commercial customers.
Service for both commercial residential include making sure all zones are operating check for leaks adjust spray nozzles in rotors making sure all irrigation heads rotate, and are not stuck or damaged making sure that we have full coverage of each Irrigation zone for lawns. In all drip irrigation is Functioning in watering the plants accordingly. Adjusting control settings to make sure you have the right watering times during the hot dry months.
Have a landscape lighting tab:
Describing what landscape lighting and what it does to enhance curb, appeal, highlight architectural, features of landscape and transferring your outdoor space into inviting visual stunning areas with low-voltage landscape lighting
And a residential snow plowing for the Falmouth Maine area. In commercial snow, plowing and snow removal covering Scarborough south portland Portland Falmouth in Cumberland Maine for commercial Snow services. From plow & Salting parking lots to Snow removing, and Snow displacement.
we started a website but it needs a up lift and bring it to pop
our web site is bluefinchyardworks311.com
here are a few websites that we really like:
www.wetlandsprayco.com
www.dewpointsprinkler.com
www.mellowmeadowwatering.com
Industry/Entity Type
Irrigation & Landscape Lighting
Coding
Coded - Design and coding required
Number of Pages Required
4 page
Font styles to use
Look and feel
Each slider illustrates characteristics of the customer's brand and the style your logo design should communicate.

```html
<!DOCTYPE html>
<html lang="en">
<head>
<meta charset="utf-8">
<title>Bluefinch Yard Works — Irrigation, Landscape Lighting & Snow Service</title>
<link href="https://fonts.googleapis.com/css2?family=Libre+Baskerville:wght@400;700&family=Poppins:wght@400;500;600;700&display=swap" rel="stylesheet">
<style>
:root{
  --green:#2fa84f;
  --green-dark:#1f7a3a;
  --green-light:#7cc46a;
  --blue:#1565c0;
  --blue-dark:#0d3f86;
  --ink:#222a2a;
  --muted:#5d6663;
  --white:#ffffff;
  --paper:#f4f7f4;
  --gold:#f5b400;
}
*{box-sizing:border-box;margin:0;padding:0}
html,body{width:1200px;height:4224px;overflow:hidden}
body{font-family:"Poppins",sans-serif;color:var(--ink);background:var(--white);position:relative}
.serif{font-family:"Libre Baskerville",serif}
.abs{position:absolute}
.btn{position:absolute;display:flex;align-items:center;justify-content:center;gap:8px;height:38px;border-radius:20px;font-size:14px;font-weight:500;color:var(--white);background:linear-gradient(90deg,var(--blue),var(--green));border:2px solid rgba(255,255,255,.85)}
.btn-green{background:var(--green)}
.photo{position:absolute}

/* header */
.site-header{position:absolute;left:0;top:0;width:1200px;height:64px;background:var(--white);z-index:3}
.brand{position:absolute;display:flex;align-items:center;gap:8px;font-weight:700;color:var(--green);white-space:nowrap}
.brand .dot{width:16px;height:16px;border-radius:50%;background:var(--green)}
.topbar-phone{position:absolute;left:880px;top:8px;width:180px;font-size:17px;font-weight:600;color:var(--blue-dark);display:flex;gap:8px;align-items:center;white-space:nowrap}
.social-dot{position:absolute;width:20px;height:20px;border-radius:50%;background:var(--blue)}
.main-nav{position:absolute;left:428px;top:38px;display:flex;gap:22px;font-size:11px;font-weight:600;text-transform:uppercase;color:var(--ink);white-space:nowrap}
.nav-cta{position:absolute;left:985px;top:34px;width:112px;height:24px;border-radius:12px;background:var(--green);color:var(--white);font-size:11px;font-weight:600;display:flex;align-items:center;justify-content:center}

/* hero */
.hero{position:absolute;left:0;top:64px;width:1200px;height:668px;background:linear-gradient(180deg,#5a6c5d 0%,#7d8a76 35%,#3f6a36 70%,#2f5a2a 100%)}
.hero h1{position:absolute;left:100px;top:200px;width:860px;font-family:"Libre Baskerville",serif;font-weight:400;font-size:42px;line-height:1.2;color:var(--white);text-transform:uppercase}
.clients-badge{position:absolute;left:920px;top:440px;width:180px;height:110px;border-radius:10px;background:rgba(255,255,255,.25);color:var(--white);padding:14px}
.clients-badge b{font-size:34px;display:block;line-height:1}
.clients-badge span{font-size:11px}
.avatar{position:absolute;top:78px;width:20px;height:20px;border-radius:50%;background:#d8c7b5;border:2px solid var(--white)}

/* about */
.about{position:absolute;left:0;top:732px;width:1200px;height:578px;background:linear-gradient(90deg,#e6f3f8 0%,#ffffff 40%,#ffffff 100%)}
.about h2{position:absolute;left:610px;top:60px;width:480px;font-family:"Libre Baskerville",serif;font-weight:400;font-size:28px;line-height:1.25;color:var(--green-dark)}
.about p{position:absolute;left:610px;width:480px;font-size:13px;line-height:1.6;color:var(--muted)}
.logo-card{position:absolute;left:220px;top:380px;width:290px;height:130px;border-radius:14px;background:linear-gradient(135deg,var(--blue),var(--green));border:4px solid var(--white);display:flex;flex-direction:column;justify-content:center;padding-left:24px;color:var(--white)}

/* residential slider */
.slide-main{position:absolute;left:100px;top:1310px;width:830px;height:548px;border-radius:16px;background:linear-gradient(180deg,#6e8a5a 0%,#7d9f5a 40%,#4f8a3c 100%);overflow:hidden}
.slide-main h3{position:absolute;left:28px;top:24px;font-family:"Libre Baskerville",serif;font-weight:400;font-size:26px;color:var(--white)}
.slide-main p{position:absolute;left:28px;top:385px;width:300px;font-size:12px;line-height:1.55;color:var(--white)}
.slide-side{position:absolute;left:945px;top:1310px;width:160px;height:548px;border-radius:16px;background:linear-gradient(180deg,#2f7bc0,#3aa34a);border:3px solid rgba(255,255,255,.8)}
.slide-side span{position:absolute;left:60px;top:40px;writing-mode:vertical-rl;font-family:"Libre Baskerville",serif;font-size:26px;color:var(--white)}

/* cta band */
.cta-band{position:absolute;left:0;top:1870px;width:1200px;height:180px;background:linear-gradient(180deg,#a9b9a6,#6d8a5e)}
.cta-band .wedge{position:absolute;left:0;top:0}
.cta-band h3{position:absolute;left:650px;top:20px;width:400px;text-align:center;font-family:"Libre Baskerville",serif;font-weight:400;font-size:26px;line-height:1.25;color:var(--white)}

/* services */
.services{position:absolute;left:0;top:2050px;width:1200px;height:510px;background:linear-gradient(180deg,#e2f0f7,#ffffff 50%,#eaf5e6)}
.section-title{font-family:"Libre Baskerville",serif;font-weight:400;font-size:30px;color:var(--green-dark)}
.service-card{position:absolute;top:110px;width:238px;height:360px;border-radius:12px;overflow:hidden;color:var(--white)}
.service-card h4{position:absolute;left:12px;top:14px;width:210px;font-family:"Libre Baskerville",serif;font-weight:400;font-size:17px;line-height:1.25}
.service-card p{position:absolute;left:14px;top:262px;width:200px;font-size:11px;line-height:1.5}
.learn-pill{position:absolute;left:14px;top:306px;width:92px;height:26px;border-radius:13px;background:var(--green);font-size:10px;font-weight:600;display:flex;align-items:center;justify-content:center}

/* works */
.works{position:absolute;left:0;top:2560px;width:1200px;height:680px;background:var(--white)}
.work{position:absolute;border-radius:10px}

/* testimonials */
.testimonials{position:absolute;left:0;top:3240px;width:1200px;height:500px;background:linear-gradient(180deg,#7f977b,#a5b79f 40%,#6f8d57)}
.testimonials h2{position:absolute;left:100px;top:20px;font-family:"Libre Baskerville",serif;font-weight:400;font-size:30px;color:var(--white)}
.review{position:absolute;top:170px;width:420px;height:220px;border-radius:12px;background:var(--white);padding:22px 24px}
.review .face{position:absolute;left:24px;top:22px;width:46px;height:46px;border-radius:50%;background:#c9b8a6}
.review h5{margin-left:60px;font-size:15px;font-weight:600}
.review .stars{margin-left:60px;color:var(--gold);font-size:15px;letter-spacing:2px}
.review p{margin-top:20px;font-size:12px;line-height:1.6;color:var(--muted)}

/* newsletter */
.newsletter{position:absolute;left:270px;top:3750px;width:660px;height:120px;background:var(--white);border-radius:6px;box-shadow:0 6px 20px rgba(0,0,0,.15);z-index:2;overflow:hidden}

/* footer */
.site-footer{position:absolute;left:0;top:3820px;width:1200px;height:404px;background:linear-gradient(90deg,var(--blue) 0%,#1d8ac0 40%,var(--green) 100%);color:var(--white)}
.footer-col h6{font-size:17px;font-weight:600;letter-spacing:1px;margin-bottom:10px}
.footer-col li{list-style:none;font-size:11px;font-weight:600;text-transform:uppercase;line-height:2}
.copy-bar{position:absolute;left:0;top:370px;width:1200px;height:34px;background:var(--white);color:var(--ink);font-size:11px;display:flex;align-items:center;justify-content:space-between;padding:0 100px}
</style>
</head>
<body>

<header class="site-header">
  <div class="brand" style="left:100px;top:14px;font-size:20px"><span class="dot"></span>Bluefinch Yard Works</div>
  <div class="topbar-phone">
    <svg width="16" height="16" viewBox="0 0 24 24"><path fill="#0d3f86" d="M6.6 10.8a15 15 0 0 0 6.6 6.6l2.2-2.2c.3-.3.7-.4 1-.2 1.1.4 2.3.6 3.6.6.6 0 1 .4 1 1V20c0 .6-.4 1-1 1A17 17 0 0 1 3 4c0-.6.4-1 1-1h3.5c.6 0 1 .4 1 1 0 1.3.2 2.5.6 3.6.1.3 0 .7-.2 1z"/></svg>
    (555) 014-2290
  </div>
  <span class="social-dot" style="left:1080px;top:10px"></span>
  <nav class="main-nav"><span>Home</span><span>About Us</span><span>Services</span><span>Residential</span><span>Commercial</span><span>Snow Removal</span></nav>
  <div class="nav-cta">Contact Us</div>
</header>

<section class="hero">
  <div class="photo" role="img" aria-label="House with porch, green lawn and running sprinklers at dusk" style="inset:0"></div>
  <h1>Irrigation System, Landscape Lighting, Residential Snow Service</h1>
  <div class="btn" style="left:100px;top:400px;width:128px">Contact Us ›</div>
  <div class="btn btn-green" style="left:242px;top:400px;width:150px">Explore Projects ›</div>
  <div class="clients-badge">
    <b>100+</b><span>Satisfied Clients</span>
    <i class="avatar" style="left:14px"></i><i class="avatar" style="left:32px"></i><i class="avatar" style="left:50px"></i><i class="avatar" style="left:68px"></i><i class="avatar" style="left:86px"></i>
  </div>
</section>

<section class="about">
  <div class="photo" role="img" aria-label="Sprinkler watering a lush green lawn" style="left:100px;top:68px;width:350px;height:330px;border-radius:12px;background:linear-gradient(180deg,#7fb3d8,#5f9e3f 55%,#3f7d2c)"></div>
  <div class="logo-card"><span style="font-size:24px;font-weight:700">Bluefinch Yard Works</span><span style="font-size:11px">Landscape &amp; Property Maintenance</span></div>
  <h2>Experienced Landscape &amp; Property Maintenance Team</h2>
  <p style="top:140px">Our team of experienced landscape property maintenance professionals is dedicated to enhancing the beauty and function of your property.</p>
  <p style="top:212px">With a keen eye for detail, we provide tailored maintenance services in the residential and commercial sectors that include lawn care, irrigation services, landscape lighting, design and installation, residential snow services and more. Whether you're looking to keep your property pristine year-round or need seasonal services, our team combines expertise and creativity to exceed your expectation.</p>
  <div class="btn" style="left:610px;top:410px;width:150px">More About Us ›</div>
</section>

<div class="slide-main">
  <div class="photo" role="img" aria-label="Sprinklers watering a residential lawn and flower beds" style="inset:0"></div>
  <h3>Residential Irrigation Service</h3>
  <p>From spring start-ups to full installs and fall winterization, we keep every zone, head and drip line in your yard working right.</p>
  <div class="btn btn-green" style="left:28px;top:470px;width:112px">Learn More ›</div>
  <svg class="abs" style="left:400px;top:510px" width="30" height="20" viewBox="0 0 30 20"><path d="M5 6l10 9 10-9" fill="none" stroke="#fff" stroke-width="3"/></svg>
</div>
<div class="slide-side"><span>Commercial Irrigation Service</span></div>

<section class="cta-band">
  <div class="photo" role="img" aria-label="Row of trees along a clubhouse lawn" style="inset:0"></div>
  <svg class="wedge" width="1200" height="180" viewBox="0 0 1200 180"><defs><linearGradient id="ctaFill" x1="0" x2="1"><stop offset="0" stop-color="#1565c0"/><stop offset="1" stop-color="#2fa84f"/></linearGradient></defs><polygon points="580,0 1200,0 1200,180 510,180" fill="url(#ctaFill)" opacity=".9"/></svg>
  <h3>Need Help for<br>Irrigation Service?</h3>
  <div class="btn btn-green" style="left:785px;top:110px;width:130px">Contact Us ›</div>
</section>

<section class="services">
  <h2 class="section-title abs" style="left:0;width:1200px;text-align:center;top:40px">Our Services</h2>
  <article class="service-card" style="left:100px;background:linear-gradient(180deg,#3f6b34,#2c5424)" role="img" aria-label="Freshly mowed striped lawn">
    <h4>Full Lawn Maintenance Services</h4>
    <p>Mowing, weed whacking, pruning, reseeding.</p>
    <span class="learn-pill">LEARN MORE</span>
  </article>
  <article class="service-card" style="left:354px;background:linear-gradient(180deg,#6c8062,#3f5a34)" role="img" aria-label="Technician installing an irrigation valve"><h4>Irrigation Install &amp; Maintenance</h4></article>
  <article class="service-card" style="left:608px;background:linear-gradient(180deg,#2a3a2a,#4e6a3e)" role="img" aria-label="Lit garden path at night"><h4>Landscape Lighting</h4></article>
  <article class="service-card" style="left:862px;background:linear-gradient(180deg,#3a3530,#6d5d4e)" role="img" aria-label="Warm outdoor lighting on a patio"><h4>Landscape Lighting</h4></article>
</section>

<section class="works">
  <h2 class="section-title abs" style="left:100px;top:28px">Our Works</h2>
  <div class="btn btn-green" style="left:896px;top:28px;width:204px">View Full Gallery ›</div>
  <div class="work" role="img" aria-label="White house with a wide green lawn" style="left:100px;top:90px;width:320px;height:510px;background:linear-gradient(180deg,#9cc3e8,#d9dfe2 35%,#5c9a3a 55%,#3f7a2a)"></div>
  <div class="work" role="img" aria-label="Snow-covered driveway after plowing" style="left:436px;top:90px;width:210px;height:245px;background:linear-gradient(180deg,#a9c4dd,#e8ecef 60%,#b4bfc6)"></div>
  <div class="work" role="img" aria-label="Tree lit by a pink landscape light" style="left:662px;top:90px;width:210px;height:245px;background:linear-gradient(180deg,#1c2b1e,#4b3a4f 50%,#2f3b2a)"></div>
  <div class="work" role="img" aria-label="Garden bed with fresh mulch" style="left:888px;top:90px;width:212px;height:245px;background:linear-gradient(180deg,#bfc9c2,#6f8a5a 60%,#4a3a2a)"></div>
  <div class="work" role="img" aria-label="Lawn with a trimmed path" style="left:436px;top:350px;width:210px;height:250px;background:linear-gradient(180deg,#8aa0b0,#6c7f54 45%,#59713d)"></div>
  <div class="work" role="img" aria-label="Large yard with fresh mulch beds and trees" style="left:662px;top:350px;width:438px;height:250px;background:linear-gradient(180deg,#c6d0d4,#7f9366 45%,#3d3428)"></div>
</section>

<section class="testimonials">
  <div class="photo" role="img" aria-label="Blurred park lawn with trees" style="inset:0"></div>
  <h2>What Happy Client Say About Us</h2>
  <article class="review" style="left:180px">
    <span class="face"></span>
    <h5>Dorian Pelley</h5><div class="stars">★★★★★</div>
    <p>The crew checked every zone, fixed two leaking heads and reset our controller for summer. Our lawn has never looked this even and green. They showed up on time, explained each step and cleaned up after. Booking our fall winterization with them too.</p>
  </article>
  <article class="review" style="left:622px">
    <span class="face"></span>
    <h5>Maren Colbeck</h5><div class="stars">★★★★★</div>
    <p>New lighting along the walkway and the front of the house changed how our home feels at night. Friendly team, clear pricing and careful work. They also plowed our drive all winter without a single missed storm. Highly recommend them.</p>
  </article>
  <svg class="abs" style="left:580px;top:448px" width="40" height="8"><circle cx="4" cy="4" r="3" fill="#fff"/><circle cx="16" cy="4" r="3" fill="#fff" opacity=".5"/><circle cx="28" cy="4" r="3" fill="#fff" opacity=".5"/></svg>
</section>

<section class="newsletter">
  <div class="photo" role="img" aria-label="Landscape lighting in a front yard at night" style="left:0;top:0;width:220px;height:120px;background:linear-gradient(135deg,#2a2f3a,#7a5d78 60%,#3a4a2c)"></div>
  <div class="abs" style="left:240px;top:16px;font-size:14px;color:var(--green)">Join Our Newsletter</div>
  <div class="abs serif" style="left:240px;top:36px;font-size:18px;color:var(--ink)">Get In Touch With Bluefinch</div>
  <div class="abs" style="left:240px;top:76px;width:260px;height:28px;border:1px solid #c8cfcc;border-radius:4px;font-size:11px;color:#8a928f;padding:6px 10px">Enter Your Email Address*</div>
  <div class="abs" style="left:510px;top:76px;width:120px;height:28px;border-radius:4px;background:var(--green);color:#fff;font-size:12px;font-weight:600;display:flex;align-items:center;justify-content:center">Subscribe</div>
</section>

<footer class="site-footer">
  <div class="brand" style="left:100px;top:90px;font-size:20px;color:#fff"><span class="dot" style="background:#fff"></span>Bluefinch Yard Works</div>
  <div class="abs" style="left:160px;top:172px;font-size:12px;font-weight:600;letter-spacing:2px">FOLLOW US</div>
  <span class="social-dot" style="left:162px;top:200px;background:#fff"></span>
  <span class="social-dot" style="left:192px;top:200px;background:#fff"></span>
  <span class="social-dot" style="left:222px;top:200px;background:#fff"></span>
  <div class="footer-col abs" style="left:550px;top:88px">
    <h6>MENU</h6>
    <ul><li>Home</li><li>About Us</li><li>Services</li><li>Residential</li><li>Commercial</li><li>Snow Removal</li></ul>
  </div>
  <div class="footer-col abs" style="left:862px;top:88px;width:240px">
    <h6>CONTACT</h6>
    <div style="font-size:14px;font-weight:600;line-height:1.3">Bluefinch Yard Works</div>
    <div style="font-size:11px;margin-top:4px">Pinecrest, Maine, United States</div>
    <div style="font-size:11px">(555) 014-2290</div>
    <div style="font-size:14px;font-weight:600;margin-top:10px">Hours</div>
    <div style="font-size:11px;line-height:1.6">Monday - Friday: 7am - 5pm<br>Saturday: By appointment<br>Sunday: Closed</div>
  </div>
  <div class="copy-bar"><span>Copyright © 2025 Bluefinch Yard Works. All Rights Reserved.</span><span>Privacy Policy · Terms &amp; Conditions</span></div>
</footer>

</body>
</html>
```